A small boutique Accounting and Mortgage Broking firm needs a business card design

Quorvel is a Brisbane based boutique accounting and mortgage broking firm. We offer a range of extensive financial services like accounting, tax consulting, book-keeping and mortgage broking.
We need a business card that stands out. The content can stay as it is on the existing card unless you recommend us to change anything on it for a better design.
Please remove the mobile number and give us a suitable format to change the details like email address and name.
Industry/Entity Type
Business
Contact Information for Business Card
Dalian Okoruwe
Quorvel Group Pty Ltd
3/412 Brackwin Rd Marrowdale QLD 4126
PO Box 829 Marrowdale QLD 4126
T 07 3184 5526
F 07 3952 1087
E dokoruwe@quorvel.net.au
Accountants Tax Agents, Mortgage Brokers
www.quorvel.net.au
Look and feel
Each slider illustrates characteristics of the customer's brand and the style your logo design should communicate.

```html
<!DOCTYPE html>
<html lang="en">
<head>
<meta charset="utf-8">
<title>Quorvel Business Card</title>
<link href="https://fonts.googleapis.com/css2?family=Montserrat:wght@400;600;700;800&family=Open+Sans:wght@400;600&display=swap" rel="stylesheet">
<style>
  :root {
    --green: #7dc242;
    --charcoal: #3d3d3f;
    --ink: #2b2b2b;
    --white: #ffffff;
    --faint: #ececec;
    --backdrop: #e4e1dc;
  }
  * { margin: 0; padding: 0; box-sizing: border-box; }
  html, body { width: 1200px; height: 1000px; overflow: hidden; }
  body { background: var(--backdrop); position: relative; font-family: "Open Sans", sans-serif; color: var(--ink); }

  .card {
    position: absolute; left: 265px; width: 668px; height: 390px;
    border-radius: 24px; overflow: hidden;
  }
  .card-front { top: 80px; background: var(--green); }
  .card-back { top: 531px; background: var(--white); }

  /* front */
  .front-brand { position: absolute; left: 0; right: 0; top: 130px; height: 124px; display: flex; align-items: center; justify-content: center; gap: 20px; }
  .brand-ring { border-radius: 50%; border-style: solid; border-color: var(--charcoal); flex: none; }
  .front-brand .brand-ring { width: 124px; height: 124px; border-width: 15px; }
  .front-brand .brand-name { font-family: "Montserrat", sans-serif; font-weight: 800; font-size: 76px; line-height: 1; color: var(--charcoal); letter-spacing: -1px; }
  .front-services { position: absolute; left: 0; right: 0; top: 333px; text-align: center; color: var(--white); font-family: "Montserrat", sans-serif; font-size: 15px; letter-spacing: 0.3px; }

  /* back */
  .back-decor { position: absolute; left: 305px; top: -30px; width: 440px; height: 440px; border-radius: 50%; border: 34px solid var(--faint); }
  .back-brand { position: absolute; left: 30px; top: 38px; height: 76px; display: flex; align-items: center; gap: 14px; }
  .back-brand .brand-ring { width: 76px; height: 76px; border-width: 10px; }
  .back-brand .brand-name { font-family: "Montserrat", sans-serif; font-weight: 800; font-size: 48px; line-height: 1; color: var(--green); letter-spacing: -0.5px; }
  .back-tagline { position: absolute; left: 30px; top: 127px; font-size: 21px; letter-spacing: 0.4px; color: var(--ink); }

  .holder-name { position: absolute; left: 30px; top: 202px; font-family: "Montserrat", sans-serif; font-weight: 700; font-size: 20px; color: var(--green); }
  .holder-rule { position: absolute; left: 30px; top: 227px; width: 606px; height: 1.5px; background: var(--ink); }

  .contact-list { position: absolute; left: 30px; top: 252px; list-style: none; font-size: 15.5px; line-height: 20.5px; }
  .contact-list li { display: flex; align-items: center; gap: 6px; }
  .contact-list svg { width: 13px; height: 13px; fill: var(--green); flex: none; }
  .contact-list strong { color: var(--green); font-weight: 700; }

  .address-block { position: absolute; left: 419px; top: 234px; font-size: 15.5px; line-height: 18.5px; }
  .address-block h3 { font-family: "Montserrat", sans-serif; font-weight: 700; font-size: 15px; color: var(--green); }
  .address-block p + h3 { margin-top: 3px; }

  .footer-band { position: absolute; left: 0; right: 0; bottom: 0; height: 35px; display: flex; }
  .footer-band .band-dark { width: 334px; background: var(--charcoal); }
  .footer-band .band-green { flex: 1; background: var(--green); }
  .footer-mark { position: absolute; left: 313px; top: 352px; width: 40px; height: 40px; border-radius: 50%; background: var(--white); border: 5px solid var(--charcoal); }
</style>
</head>
<body>

<section class="card card-front" aria-label="Business card front">
  <div class="front-brand">
    <span class="brand-ring"></span>
    <span class="brand-name">quorvel</span>
  </div>
  <p class="front-services">Accountants Tax Agents, Mortgage Brokers</p>
</section>

<section class="card card-back" aria-label="Business card back">
  <div class="back-decor"></div>

  <div class="back-brand">
    <span class="brand-ring"></span>
    <span class="brand-name">quorvel</span>
  </div>
  <p class="back-tagline">CLARITY. CARE. PROGRESS.</p>

  <h2 class="holder-name">Dalian Okoruwe</h2>
  <div class="holder-rule"></div>

  <ul class="contact-list">
    <li><svg viewBox="0 0 24 24"><path d="M6.6 10.8c1.4 2.8 3.8 5.1 6.6 6.6l2.2-2.2c.3-.3.7-.4 1-.2 1.1.4 2.3.6 3.6.6.6 0 1 .4 1 1V20c0 .6-.4 1-1 1C10.6 21 3 13.4 3 4c0-.6.4-1 1-1h3.5c.6 0 1 .4 1 1 0 1.3.2 2.5.6 3.6.1.3 0 .7-.2 1z"/></svg><span>07 3184 5526</span></li>
    <li><svg viewBox="0 0 24 24"><path d="M6 2h12v5H6zM3 8h18c1 0 2 1 2 2v7h-4v5H5v-5H1v-7c0-1 1-2 2-2zm4 8v4h10v-4z"/></svg><span>07 3952 1087</span></li>
    <li><svg viewBox="0 0 24 24"><path d="M2 5h20v14H2zm2 2v.5l8 5 8-5V7l-8 5z"/></svg><span>dokoruwe@quorvel.net.au</span></li>
    <li><svg viewBox="0 0 24 24"><path d="M12 2a10 10 0 1 0 0 20 10 10 0 0 0 0-20zm6.9 6h-2.9a15 15 0 0 0-1.4-3.6A8 8 0 0 1 18.9 8zM12 4c.8 1.2 1.5 2.5 1.9 4h-3.8c.4-1.5 1.1-2.8 1.9-4zM4.3 14a8 8 0 0 1 0-4h3.3a16 16 0 0 0 0 4zm.8 2h2.9c.3 1.3.8 2.5 1.4 3.6A8 8 0 0 1 5.1 16zM8 8H5.1a8 8 0 0 1 4.3-3.6C8.8 5.5 8.3 6.7 8 8zm4 12c-.8-1.2-1.5-2.5-1.9-4h3.8c-.4 1.5-1.1 2.8-1.9 4zm2.3-6H9.7a14 14 0 0 1 0-4h4.6a14 14 0 0 1 0 4zm.3 5.6c.6-1.1 1.1-2.3 1.4-3.6h2.9a8 8 0 0 1-4.3 3.6zm1.8-5.6a16 16 0 0 0 0-4h3.3a8 8 0 0 1 0 4z"/></svg><span>www.<strong>quorvel</strong>.net.au</span></li>
  </ul>

  <div class="address-block">
    <h3>Mailing Address</h3>
    <p>PO Box 829 Marrowdale<br>QLD 4126</p>
    <h3>Location Address</h3>
    <p>3/412 Brackwin Rd Marrowdale<br>QLD 4126</p>
  </div>

  <div class="footer-band">
    <div class="band-dark"></div>
    <div class="band-green"></div>
  </div>
  <span class="footer-mark"></span>
</section>

</body>
</html>
```